Packaging box design for start up candle company based in Sydney Australia

I need an eye catching box design for my candle company called Morningside Wickery. We specialise only in delicious cake and cocktail scented candles. I want to convey a sense of elegant whimsy.
I have a logo and a style guide which I'm happy with, but need to complete the brand with a stunning box design.
I'd like the same design for two different sized boxes.

```html
<!DOCTYPE html>
<html lang="en">
<head>
<meta charset="utf-8">
<title>Morningside Wickery – Candle Box</title>
<link rel="stylesheet" href="https://fonts.googleapis.com/css2?family=Cormorant+Garamond:wght@500&family=Barlow:wght@400&display=swap">
<style>
  :root {
    --bg: #ffffff;
    --panel: #efa39c;
    --panel-top: #f4b2ab;
    --band: #e58a7c;
    --ink: #a8463f;
    --ink-soft: #b9625a;
    --fold: #d98d85;
  }
  * { box-sizing: border-box; margin: 0; padding: 0; }
  html, body { width: 1200px; height: 675px; overflow: hidden; background: var(--bg); }
  .canvas { position: relative; width: 1200px; height: 675px; }

  .panel { position: absolute; background: var(--panel); overflow: hidden; }
  .panel-top   { left: 340px; top: 50px;  width: 260px; height: 260px; background: var(--panel-top); border-bottom: 1px dashed var(--fold); }
  .panel-front { left: 340px; top: 310px; width: 260px; height: 315px; }
  .panel-side  { left: 600px; top: 310px; width: 260px; height: 315px; border-left: 1px dashed var(--fold); }

  .band {
    position: absolute; left: 0; right: 0; bottom: 0; height: 62px;
    background: var(--band);
  }
  .band-details {
    position: absolute; left: 0; right: 0; top: 26px;
    display: flex; justify-content: center; gap: 40px;
    font-family: "Barlow", sans-serif; font-size: 7px; letter-spacing: 1.4px;
    color: var(--ink-soft);
  }

  .tagline {
    position: absolute; left: 0; right: 0; top: 40px; text-align: center;
    font-family: "Barlow", sans-serif; font-size: 8px; letter-spacing: 3px;
    color: var(--ink-soft);
  }

  .brand-name {
    position: absolute; left: 0; right: 0; text-align: center;
    font-family: "Cormorant Garamond", serif; font-weight: 500;
    color: var(--ink); text-transform: uppercase; line-height: 1;
  }
  .brand-name .line-1 { display: block; }
  .brand-name .line-2 { display: block; }

  .panel-front .brand-name { top: 130px; }
  .panel-front .brand-name .line-1 { font-size: 25px; letter-spacing: 3px; }
  .panel-front .brand-name .line-2 { font-size: 17px; letter-spacing: 7px; margin-top: 4px; }

  .panel-top .brand-name { top: 100px; }
  .panel-top .brand-name .line-1 { font-size: 17px; letter-spacing: 2.5px; }
  .panel-top .brand-name .line-2 { font-size: 12px; letter-spacing: 5px; margin-top: 3px; }

  .care-copy {
    position: absolute; left: 22px; right: 22px; top: 105px;
    font-family: "Barlow", sans-serif; font-size: 7px; line-height: 1.55;
    letter-spacing: 0.6px; text-align: justify; text-transform: uppercase;
    color: var(--ink-soft);
  }
</style>
</head>
<body>
  <main class="canvas">
    <section class="panel panel-top" aria-label="Box lid">
      <h2 class="brand-name"><span class="line-1">Morningside</span><span class="line-2">Wickery</span></h2>
    </section>

    <section class="panel panel-front" aria-label="Box front">
      <p class="tagline">SCENTED WAX CANDLE</p>
      <h1 class="brand-name"><span class="line-1">Morningside</span><span class="line-2">Wickery</span></h1>
      <div class="band">
        <div class="band-details"><span>7OZ GLASS</span><span>36 HR BURN</span></div>
      </div>
    </section>

    <section class="panel panel-side" aria-label="Box side">
      <p class="care-copy">Hand poured in small batches using a soft blend of soy and coconut wax. Trim the wick to five millimetres before each lighting and burn for no more than four hours at a time. Keep away from drafts, children and pets. Never leave a burning candle unattended. Enjoy the glow and let each sweet note fill the room slowly.</p>
      <div class="band"></div>
    </section>
  </main>
</body>
</html>
```